Flyer Design Project for our Parenting Psychologists at the Wellmind Counselling Centre

At the Wellmind Counselling Centre we have expert Parenting Psychologists.

Parenting Psychologists provide practical, step by step assistance to parents who are struggling with their children's behavioural and emotional problems.

We need a DL size brochure that will be appealing to parents. The brochure will be on show in schools, kindergartens and GP clinics.

In terms of style it will be in line with our website and stationery that I will attach.

www.wellmindcounsellingcentre.com.au

Hi Everyone,
Thanks for putting forward your proposals, there are a couple there that I am very interested in. I am looking to see if there is a way that I can change my brief to guaranteed as I am definitely going to be using one of the designs for sure.
I have emailed ArtForge and as soon as I get an answer I will change it if I can.
If anyone out there already knows the answer please let me know :-)
Thanks,
Marcie.

Hi Again,

I worked it out myself!!

I have now changed this to a committed project.

Kind regards,
Marcie.

Reason: I have 46 designs now and need more time to work out which is best!

Target Market(s)

The target will be educated professional parents motivated to get professional help. And doctors and teachers who will pass on the brochures 2 parents

Industry/Entity Type

Health

Requirements
Must have
• I want one DL size brochure. Back and front.

We need text (below) and our contact details. Our logo.

6352 1840
Suite 1, 2087 Tamworth Rd, Tamworth North 3118

Text:
Parents want the best for their kids. They want kids that are happy, healthy and well behaved.

So why is it so hard? Parents of toddlers, primary schoolers and teenagers alike say that they are frustrated by constant nagging, bribing and yelling, they don't know what to try next. Some parents worry that their children are unhappy. Struggling at school, not making friends or coping with bigger problems.

The good news is that getting your children to behave more co-operatively doesn't need to be difficult or mysterious. We all know that kids don't come with manuals, but there are skills every parent can learn to make parenting easier. In a few sessions with a Parenting Psychologist, you will receive step by step guidance in how to talk to your children in a way that will be much more effective getting them to behave in a respectful and co-operative way around the home and in public. You will learn how to help your child cope with problems they are going through. They can help you reconnect with your kids so you can enjoy being a parent again.

Nice to have
• Themes consistent with our website
and letterhead, business cards. I will attach these.
Should not have
• I don't want it to look too cluttered so if the text I have provided up above looks too crowded then I will edit it.

```html
<!DOCTYPE html>
<html lang="en">
<head>
<meta charset="utf-8">
<title>Wellmind Counselling Centre – Parenting DL Flyer</title>
<link rel="stylesheet" href="https://fonts.googleapis.com/css2?family=Arimo:ital,wght@0,400;0,700;1,700&family=Roboto+Condensed:wght@400;700&family=Philosopher:wght@700&display=swap">
<style>
  :root {
    --canvas: #000000;
    --green: #0e7060;
    --white: #ffffff;
    --ink: #1e1f24;
    --stripe-1: #6f9aab;
    --stripe-2: #7cc3c8;
    --stripe-3: #6fa6a6;
    --stripe-4: #7a8a90;
    --lilac-top: #dfe4ee;
    --lilac-bottom: #b6bde0;
    --box-top: #e4e8f1;
    --box-bottom: #c1c6db;
  }
  * { box-sizing: border-box; margin: 0; padding: 0; }
  html, body {
    width: 1200px; height: 1176px; overflow: hidden;
    background: var(--canvas);
  }
  .sheet { position: relative; width: 1200px; height: 1176px; }

  .panel {
    position: absolute; top: 81px;
    width: 467px; height: 987px;
    overflow: hidden;
  }
  .panel--back { left: 111px; background: var(--green); color: var(--white); }
  .panel--front {
    left: 635px;
    background: linear-gradient(180deg, var(--lilac-top) 35%, var(--lilac-bottom) 100%);
    color: var(--ink);
  }

  .stripe { position: absolute; left: 0; width: 100%; height: 40px; display: flex; }
  .stripe--top { top: 0; }
  .stripe--bottom { bottom: 0; }
  .stripe span { flex: 1; }
  .stripe span:nth-child(1) { background: var(--stripe-1); }
  .stripe span:nth-child(2) { background: var(--stripe-2); }
  .stripe span:nth-child(3) { background: var(--stripe-3); }
  .stripe span:nth-child(4) { background: var(--stripe-4); }
  .stripe span:nth-child(5) { background: var(--stripe-2); }

  /* Back */
  .intro {
    position: absolute; left: 33px; right: 29px; top: 62px;
    font-family: "Arimo", Arial, sans-serif;
    font-size: 15.4px; line-height: 23px;
    text-align: justify;
  }
  .intro__lead { font-size: 30px; letter-spacing: -0.2px; }
  .web {
    position: absolute; left: 0; right: 0; top: 438px;
    text-align: center;
    font-family: "Roboto Condensed", Arial, sans-serif;
    font-weight: 700; font-size: 21.5px; letter-spacing: 0.6px;
  }
  .services {
    position: absolute; left: 27px; top: 494px;
    width: 413px; height: 196px;
    border-radius: 14px;
    background: linear-gradient(180deg, var(--box-top), var(--box-bottom));
    color: var(--ink);
    padding: 12px 14px 0 14px;
  }
  .services__intro {
    font-family: "Arimo", Arial, sans-serif;
    font-size: 18px; line-height: 23px; color: #34363c;
  }
  .services__list { list-style: none; margin-top: 8px; }
  .services__item {
    display: flex; align-items: center; gap: 12px;
    font-family: "Roboto Condensed", Arial, sans-serif;
    font-weight: 700; font-size: 23px; line-height: 36.5px;
  }
  .services__dot {
    width: 14px; height: 14px; border-radius: 50%;
    border: 2.5px solid var(--green); flex: none;
  }
  .contact { position: absolute; left: 0; right: 0; text-align: center; }
  .contact__label { top: 757px; font-family: "Arimo", Arial, sans-serif; font-size: 19.5px; }
  .contact__phone {
    top: 784px; font-family: "Roboto Condensed", Arial, sans-serif;
    font-weight: 700; font-size: 40px; letter-spacing: 0.5px;
  }
  .contact__name { top: 871px; font-family: "Arimo", Arial, sans-serif; font-weight: 700; font-size: 24px; }
  .contact__email { top: 908px; font-family: "Arimo", Arial, sans-serif; font-size: 15.5px; }

  /* Front */
  .photo {
    position: absolute; left: 0; top: 0; width: 100%; height: 314px;
    background: linear-gradient(160deg, #8fb35a 0%, #5e8a36 40%, #b98a6a 65%, #6d8fb6 100%);
  }
  .headline {
    position: absolute; left: 0; right: 0; top: 345px;
    text-align: center;
    font-family: "Roboto Condensed", Arial, sans-serif;
    font-weight: 700; font-size: 40px; line-height: 46px;
    color: #25262b;
  }
  .subhead {
    position: absolute; left: 0; right: 0; top: 446px;
    text-align: center;
    font-family: "Philosopher", Georgia, sans-serif;
    font-weight: 700; font-size: 29px; line-height: 38px;
  }
  .body-copy {
    position: absolute; left: 30px; right: 30px; top: 573px;
    font-family: "Arimo", Arial, sans-serif;
    font-size: 15.6px; line-height: 25px;
    text-align: justify;
  }
  .brand {
    position: absolute; left: 0; right: 0; top: 826px;
    display: flex; align-items: center; justify-content: center; gap: 14px;
  }
  .brand__mark { width: 30px; height: 30px; border-radius: 50%; background: var(--green); }
  .brand__name {
    font-family: "Arimo", Arial, sans-serif; font-weight: 700;
    font-size: 24px; color: var(--green);
  }
  .address {
    position: absolute; left: 0; right: 0; top: 908px;
    text-align: center;
    font-family: "Arimo", Arial, sans-serif; font-size: 15.2px;
  }

  .label {
    position: absolute; top: 1094px; width: 467px;
    text-align: center; color: var(--white);
    font-family: "Arimo", Arial, sans-serif; font-weight: 700; font-style: italic;
    font-size: 40px; letter-spacing: 1px;
  }
  .label--back { left: 111px; }
  .label--front { left: 635px; }
</style>
</head>
<body>
<main class="sheet">

  <section class="panel panel--back">
    <div class="stripe stripe--top"><span></span><span></span><span></span><span></span><span></span></div>

    <p class="intro"><span class="intro__lead">The good news is that</span> getting your children to behave more co-operatively doesn't need to be difficult or mysterious. We all know that kids don't come with manuals, but there are skills every parent can learn to make parenting easier. In a few sessions with a Parenting Psychologist, you will receive step by step guidance in how to talk to your children in a way that will be much more effective getting them to behave in a respectful and co-operative way around the home and in public. You will learn how to help your child cope with problems they are going through. They can help you reconnect with your kids so you can enjoy being a parent again.</p>

    <p class="web">www.wellmindcounsellingcentre.com.au</p>

    <div class="services">
      <p class="services__intro">Our expert psychology team has specific training and experience in three key areas:</p>
      <ul class="services__list">
        <li class="services__item"><span class="services__dot"></span>Disordered Eating</li>
        <li class="services__item"><span class="services__dot"></span>Chronic Pain &amp; Illness</li>
        <li class="services__item"><span class="services__dot"></span>Pregnancy &amp; Parenting</li>
      </ul>
    </div>

    <p class="contact contact__label">Appointment &amp; Enquiries</p>
    <p class="contact contact__phone">(03) 6352 1840</p>
    <p class="contact contact__name">Wellmind Counselling Centre</p>
    <p class="contact contact__email">email: info@wellmindcounsellingcentre.com.au</p>

    <div class="stripe stripe--bottom"><span></span><span></span><span></span><span></span><span></span></div>
  </section>

  <section class="panel panel--front">
    <div class="photo" role="img" aria-label="Photo of a smiling mother and her toddler on a picnic blanket in a sunny park with a fruit basket"></div>

    <h1 class="headline">PARENTS WANT THE<br>BEST FOR THEIR KIDS.</h1>
    <p class="subhead">They want kids that are happy,<br>healthy and well behaved.</p>

    <p class="body-copy">So why is it so hard? Parents of toddlers, primary schoolers and teenagers alike say that they are frustrated by constant nagging, bribing and yelling, they don't know what to try next. Some parents worry that their children are unhappy. Struggling at school, not making friends or coping with bigger problems.</p>

    <div class="brand">
      <span class="brand__mark"></span>
      <span class="brand__name">Wellmind Counselling Centre</span>
    </div>
    <p class="address">Suite 1, 2087 Tamworth Road, Tamworth North&nbsp; Victoria&nbsp; 3118</p>

    <div class="stripe stripe--bottom"><span></span><span></span><span></span><span></span><span></span></div>
  </section>

  <p class="label label--back">BACK</p>
  <p class="label label--front">FRONT</p>

</main>
</body>
</html>
```